Belmora - Medical Device Company Needs Box Refined

We are a medical device company needing our packaging refined. This she be clean and sophisticated. The logo must not be change. Please see the attached sample for baseline and sizing.

It Company

```html
<!DOCTYPE html>
<html lang="en">
<head>
<meta charset="utf-8">
<title>Belmora – Intraocular Lens Carton Dieline</title>
<link rel="stylesheet" href="https://fonts.googleapis.com/css2?family=Arimo:wght@400;700&display=swap">
<style>
  :root {
    --stage: #e4e6e9;
    --paper: #ffffff;
    --wash-top: #ffffff;
    --wash-bottom: #dcebf7;
    --brand-blue: #1f5fae;
    --accent-yellow: #f2d21b;
    --ink-grey: #6f7377;
    --ink-dark: #3c3f42;
    --fold: #c9d6e2;
    --edge: #b9c4cf;
  }
  html, body {
    margin: 0;
    padding: 0;
    width: 1200px;
    height: 736px;
    overflow: hidden;
    background: var(--stage);
    font-family: "Arimo", Arial, sans-serif;
  }
  .canvas {
    position: relative;
    width: 1200px;
    height: 736px;
  }
  .dieline {
    position: absolute;
    left: 280px;
    top: 12px;
    width: 640px;
    height: 712px;
  }
  .panel-face { fill: var(--paper); stroke: var(--edge); stroke-width: 0.8; }
  .panel-wash { fill: url(#backgroundWash); }
  .fold-line { stroke: var(--fold); stroke-width: 0.7; }
  .brand-name { font-family: "Arimo", Arial, sans-serif; font-weight: 400; fill: var(--brand-blue); }
  .brand-dot { fill: none; stroke: var(--accent-yellow); stroke-width: 2; }
  .product-title { font-size: 10px; fill: var(--ink-grey); letter-spacing: 0.2px; }
  .contents-label { font-size: 6px; fill: #ffffff; }
  .contents-value { font-size: 8.5px; font-weight: 700; fill: #ffffff; letter-spacing: 0.4px; }
  .info-text { font-size: 7px; fill: var(--ink-dark); }
  .maker-text { font-size: 6.5px; fill: var(--ink-dark); }
  .icon { fill: none; stroke: var(--ink-dark); stroke-width: 0.7; }
  .icon-label { font-size: 4px; fill: var(--ink-dark); font-weight: 700; }
</style>
</head>
<body>
<main class="canvas">
  <svg class="dieline" viewBox="0 0 640 712" xmlns="http://www.w3.org/2000/svg">
    <defs>
      <linearGradient id="backgroundWash" x1="0" y1="0" x2="0" y2="1">
        <stop offset="0" stop-color="var(--wash-top)"/>
        <stop offset="1" stop-color="var(--wash-bottom)"/>
      </linearGradient>
      <linearGradient id="contentsBand" x1="0" y1="0" x2="1" y2="0">
        <stop offset="0" stop-color="#1b5aa8"/>
        <stop offset="0.7" stop-color="#1f5fae"/>
        <stop offset="1" stop-color="#5d8fcc"/>
      </linearGradient>
      <radialGradient id="eyeTone" cx="0.45" cy="0.5" r="0.55">
        <stop offset="0" stop-color="#1f5fae"/>
        <stop offset="0.6" stop-color="#6b97cf"/>
        <stop offset="1" stop-color="#ffffff" stop-opacity="0"/>
      </radialGradient>
      <radialGradient id="lensTone" cx="0.5" cy="0.5" r="0.5">
        <stop offset="0" stop-color="#eef3f7"/>
        <stop offset="0.8" stop-color="#c8d6e2"/>
        <stop offset="1" stop-color="#c8d6e2" stop-opacity="0"/>
      </radialGradient>
    </defs>

    <!-- Top tuck flap -->
    <g class="tuck-flap-top">
      <path class="panel-face" d="M61,83 L61,14 Q61,8 67,8 L143,0 L490,0 L600,8 Q613,8 613,14 L613,83 Z"/>
      <line class="fold-line" x1="143" y1="0" x2="143" y2="83"/>
      <line class="fold-line" x1="490" y1="0" x2="490" y2="83"/>
      <g transform="rotate(180 370 40)">
        <text class="maker-text" x="268" y="30">Northvale Optics Ltd.</text>
        <text class="maker-text" x="268" y="40">Harlow House, Marsh Lane, Kendrick, Westshire</text>
        <text class="maker-text" x="268" y="50">KW4 2RP, United Kingdom</text>
        <text class="maker-text" x="268" y="60">Website: www.northvale-optics.com E-mail: info@northvale-optics.com</text>
      </g>
    </g>

    <!-- Front band: glue flap, front, side -->
    <g class="front-band">
      <rect class="panel-face" x="0" y="93" width="638" height="245" rx="14"/>
      <rect class="panel-wash" x="0.5" y="93.5" width="637" height="244" rx="14"
            role="img" aria-label="Soft light-blue background wash"/>
      <line class="fold-line" x1="48" y1="93" x2="48" y2="338"/>
      <line class="fold-line" x1="143" y1="93" x2="143" y2="338"/>
      <line class="fold-line" x1="490" y1="93" x2="490" y2="338"/>

      <g class="brand-mark" transform="translate(156,135)">
        <circle class="brand-dot" cx="6" cy="-6" r="6"/>
        <text class="brand-name" x="16" y="0" font-size="17">Belmora</text>
      </g>
      <text class="product-title" x="246" y="130">HYDROPHILIC ACRYLIC INTRAOCULAR LENS</text>

      <g role="img" aria-label="Halftone illustration of a human eye in brand blue">
        <ellipse cx="357" cy="225" rx="115" ry="75" fill="url(#eyeTone)"/>
      </g>

      <rect x="143" y="305" width="347" height="33" fill="url(#contentsBand)"/>
      <text class="contents-label" x="157" y="316">CONTENTS:</text>
      <text class="contents-value" x="157" y="328">ONE INTRAOCULAR LENS</text>

      <g class="side-symbols">
        <g transform="rotate(90 566 115)">
          <text class="icon-label" x="556" y="114">Single</text>
          <text class="icon-label" x="556" y="119">Use Only</text>
        </g>
        <circle class="icon" cx="566" cy="136" r="4.5"/>
        <path class="icon" d="M563,133 L569,139 M569,133 L563,139"/>
        <circle class="icon" cx="566" cy="159" r="4.5"/>
        <path class="icon" d="M563,156 L569,162"/>
        <circle class="icon" cx="566" cy="183" r="4.5"/>
        <path class="icon" d="M563,180 L569,186"/>
        <path class="icon" d="M561,213 L571,208 L571,218 Z"/>
        <rect class="icon" x="561" y="228" width="9" height="22"/>
        <g transform="rotate(-90 530 305)">
          <circle class="brand-dot" cx="512" cy="300" r="4"/>
          <text class="brand-name" x="518" y="304" font-size="11">Belmora</text>
        </g>
      </g>
    </g>

    <!-- Lower dust flap / box top -->
    <g class="box-top-panel">
      <path class="panel-face" d="M61,346 L613,346 L613,412 L600,424 L490,431 L143,431 L72,424 L61,412 Z"/>
      <rect class="panel-wash" x="143.5" y="346.5" width="346" height="84"
            role="img" aria-label="Soft light-blue background wash"/>
      <line class="fold-line" x1="143" y1="346" x2="143" y2="431"/>
      <line class="fold-line" x1="490" y1="346" x2="490" y2="431"/>
      <g class="brand-mark" transform="translate(158,382)">
        <circle class="brand-dot" cx="6" cy="-6" r="6"/>
        <text class="brand-name" x="16" y="0" font-size="17">Belmora</text>
      </g>
      <text class="product-title" x="163" y="418">HYDROPHILIC ACRYLIC INTRAOCULAR LENS</text>
      <g role="img" aria-label="Photograph of a clear foldable intraocular lens with haptics">
        <ellipse cx="422" cy="378" rx="42" ry="22" fill="url(#lensTone)"/>
      </g>
    </g>

    <!-- Back panel -->
    <g class="back-panel">
      <rect class="panel-face" x="143" y="431" width="347" height="279"/>
      <rect class="panel-wash" x="143.5" y="431.5" width="346" height="278"
            role="img" aria-label="Soft light-blue background wash"/>
      <g class="brand-mark" transform="translate(262,485)">
        <circle class="brand-dot" cx="6" cy="-6" r="6"/>
        <text class="brand-name" x="16" y="0" font-size="17">Belmora</text>
      </g>

      <g class="usage-list">
        <rect class="icon" x="236" y="521" width="16" height="8"/>
        <text class="icon-label" x="247" y="527">i</text>
        <text class="info-text" x="260" y="527">Contains:</text>
        <text class="info-text" x="260" y="535">One sterile hydrophilic foldable aspheric intraocular</text>
        <text class="info-text" x="260" y="543">lens, Patient ID Card, Product inserts</text>

        <circle class="icon" cx="244" cy="551" r="4.5"/>
        <path class="icon" d="M241,548 L247,554"/>
        <text class="info-text" x="260" y="554">Do not use if the packaging is opened or damaged.</text>

        <circle class="icon" cx="244" cy="564" r="4.5"/>
        <path class="icon" d="M241,561 L247,567"/>
        <text class="info-text" x="260" y="567">Do not resterile by any method.</text>

        <path class="icon" d="M241,575 L247,575 L244,581 Z M244,581 L244,584"/>
        <text class="info-text" x="260" y="581">Should not use after the specified month and year</text>

        <path class="icon" d="M238,599 L244,589 L250,599 Z"/>
        <text class="icon-label" x="243" y="598">!</text>
        <text class="info-text" x="260" y="597">Attention! see instruction for use</text>
        <text class="info-text" x="260" y="606">Store in cool and dry place.</text>

        <circle class="icon" cx="244" cy="613" r="4.5"/>
        <text class="icon-label" x="242.5" y="615" font-size="5">2</text>
        <text class="info-text" x="260" y="616">FOR SINGLE USE ONLY</text>

        <rect class="icon" x="220" y="623" width="32" height="8"/>
        <text class="icon-label" x="223" y="629">STERILE</text>
        <text class="icon-label" x="247" y="629">i</text>
        <text class="info-text" x="260" y="629">Intraocular lens sterilized by steam.</text>
      </g>
      <line class="fold-line" x1="143" y1="697" x2="490" y2="697"/>
    </g>
  </svg>
</main>
</body>
</html>
```